Arts Education Non-Profit needs 4-Page PDF Design

We're a global arts and education nonprofit based in New York. We're looking for a 4-page pdf design for our "A Year with Lantern 7" introductory packet.

The design should feature the company logo, our brand color (purple), a circle motif (if possible) and should also adhere to our current brand guidelines: https://stylekitt.example/lantern-7

Our goal is to create a well-designed document that is eye-catching enough to attract and hold the attention of busy educators.

We've also attached a few photos (optional)

Target Market(s)

Teachers and School Admistrators

Industry/Entity Type

Education

Colors
0054AA
0677BA
7BADD7
CADEEF
E8F1F8
00AB8E
00BBA5
67D7C9
C6EFE9
E9F9F6
FFF300
FFF600
FEFA6F
FFFEC7
FFFEE8
F0912C
F2A743
F7CA91
FBE8D2
FDF5EE
EB3D1F
EC4F4E
F09395
F8D3D4
FCEDEE
6B429C
8869AF
B7A5CE
E3DAEB
F3F0F8

Requirements
Nice to have
• circle motif from brand guidelines

```html
<!DOCTYPE html>
<html lang="en">
<head>
<meta charset="utf-8">
<title>A Year with Lantern 7 – Introductory Packet</title>
<link href="https://fonts.googleapis.com/css2?family=Lora:wght@400;500;600&family=Lato:wght@400;700&display=swap" rel="stylesheet">
<style>
  :root{
    --stage:#595959;
    --purple:#6B429C;
    --violet:#7E4FB5;
    --red:#EC4F4E;
    --red-deep:#DB3B36;
    --mustard:#DBB741;
    --orange:#F0912C;
    --ink:#1E1E1E;
    --white:#FFFFFF;
    --serif:'Lora', Georgia, serif;
    --sans:'Lato', Arial, sans-serif;
  }
  *{box-sizing:border-box;margin:0;padding:0}
  html,body{width:1200px;height:900px;overflow:hidden;background:var(--stage)}
  h1,h2,h3{font-weight:400}
  .stage{position:relative;width:1200px;height:900px}
  .page{position:absolute;top:97px;width:508px;height:715px;background:var(--white);overflow:hidden;box-shadow:0 4px 14px rgba(0,0,0,.35);font-family:var(--sans);color:var(--ink)}
  .page--cover{left:68px}
  .page--phases{left:643px}
  .page__art{position:absolute;inset:0}
  .abs{position:absolute}
  .photo{position:absolute;border-radius:50%}

  /* cover */
  .logo-disc{left:35px;top:66px;width:104px;height:104px;border-radius:50%;background:var(--white);display:flex;align-items:center;justify-content:center;font-family:var(--serif);color:var(--purple);font-size:19px;font-weight:400}
  .cover-kicker{left:10px;top:200px;width:160px;text-align:center;color:var(--white);font-family:var(--serif);font-weight:400;line-height:1.05}
  .cover-kicker .big{display:block;font-size:29px;letter-spacing:.5px}
  .cover-kicker .small{display:block;font-size:19px;margin-top:3px}
  .band-title{left:0;top:378px;width:508px;height:37px;display:flex;align-items:center;justify-content:center;color:var(--white);font-family:var(--serif);font-size:22px}
  .intro{left:22px;top:421px;width:466px;font-size:8.6px;line-height:1.45;text-align:justify;text-align-last:center}
  .band-outcomes{left:0;top:471px;width:508px;height:29px;display:flex;align-items:center;justify-content:center;color:var(--white);font-family:var(--serif);font-size:22px}
  .outcomes-lead{left:0;top:508px;width:508px;text-align:center;font-size:11.5px;font-weight:700}
  .outcomes{left:34px;top:534px;width:450px;display:grid;grid-template-columns:1fr 1fr;column-gap:18px;font-size:7.8px;line-height:1.3}
  .outcomes ul{list-style:none}
  .outcomes li{position:relative;padding-left:14px;margin-bottom:5.5px}
  .outcomes li::before{content:"";position:absolute;left:0;top:2px;width:5px;height:5px;border-radius:50%;background:var(--orange)}
  .footer-text{top:684px;height:18px;line-height:18px;color:var(--white);font-family:var(--serif);font-size:12.5px;white-space:nowrap}
  .footer-call{left:0;width:272px;text-align:right}
  .footer-web{left:288px}

  /* phases page */
  .lead{left:30px;top:222px;width:452px;text-align:justify;text-align-last:center;font-size:10.4px;font-weight:700;line-height:1.35}
  .pill{left:50%;transform:translateX(-50%);height:22px;padding:0 16px;border-radius:11px;color:var(--white);font-family:var(--serif);font-size:16px;display:flex;align-items:center;white-space:nowrap}
  .pill--red{top:277px;background:var(--red)}
  .pill--mustard{top:580px;background:var(--mustard)}
  .phase-box{left:25px;top:290px;width:460px;height:274px;border:2px solid var(--mustard);border-radius:14px}
  .phase-intro{left:52px;top:313px;width:406px;text-align:center;font-size:6.6px;line-height:1.45}
  .skill{font-size:6.6px;line-height:1.35}
  .skill h3{font-family:var(--serif);font-size:10px;line-height:1.15;padding-bottom:3px;margin-bottom:7px;border-bottom:1px dotted var(--red)}
  .skill h3.purple{color:var(--purple)}
  .skill h3.red{color:var(--red-deep)}
  .skill ul{list-style:none}
  .skill li{position:relative;padding-left:7px;margin-bottom:5px}
  .skill li::before{content:"•";position:absolute;left:0}
  .skill-1{left:47px;top:366px;width:140px}
  .skill-2{left:238px;top:366px;width:230px}
  .skill-2 .cols{display:grid;grid-template-columns:1fr 1fr;gap:10px}
  .skill-3{left:47px;top:466px;width:175px}
  .skill-4{left:259px;top:466px;width:190px}
  .divider{background:#9A9A9A;width:1px}
  .phase2-text{left:26px;top:611px;width:456px;text-align:center;font-size:6.6px;line-height:2}
</style>
</head>
<body>
<main class="stage">

  <!-- Page 1: cover -->
  <section class="page page--cover">
    <svg class="page__art" viewBox="0 0 508 715" aria-hidden="true">
      <rect x="0" y="0" width="322" height="365" fill="var(--purple)"/>
      <rect x="322" y="0" width="186" height="365" fill="var(--red)"/>
      <circle cx="500" cy="-5" r="58" fill="var(--purple)"/>
      <circle cx="40" cy="-15" r="58" fill="none" stroke="var(--mustard)" stroke-width="3" stroke-dasharray="0 8" stroke-linecap="round"/>
      <circle cx="324" cy="165" r="176" fill="none" stroke="var(--white)" stroke-width="1.8"/>
      <circle cx="122" cy="355" r="48" fill="var(--mustard)"/>
      <circle cx="122" cy="355" r="58" fill="none" stroke="var(--mustard)" stroke-width="3" stroke-dasharray="0 8" stroke-linecap="round"/>
      <circle cx="505" cy="345" r="55" fill="var(--red-deep)"/>
      <circle cx="420" cy="255" r="26" fill="none" stroke="var(--mustard)" stroke-width="4" stroke-dasharray="0 9" stroke-linecap="round"/>
      <rect x="0" y="365" width="508" height="13" fill="var(--white)"/>
      <rect x="0" y="378" width="508" height="37" fill="var(--mustard)"/>
      <rect x="0" y="471" width="508" height="29" fill="var(--purple)"/>
      <path d="M0 672 Q254 630 508 672 L508 715 L0 715Z" fill="var(--mustard)"/>
      <path d="M0 676 Q254 640 508 676 L508 715 L0 715Z" fill="var(--red)"/>
      <rect x="276" y="660" width="232" height="55" fill="var(--red-deep)"/>
      <path d="M0 676 Q254 640 508 676 L508 650 L0 650Z" fill="var(--white)"/>
      <path d="M0 672 Q254 630 508 672 L508 676 Q254 640 0 676Z" fill="var(--mustard)"/>
      <circle cx="30" cy="712" r="45" fill="var(--mustard)"/>
      <circle cx="30" cy="712" r="55" fill="none" stroke="var(--mustard)" stroke-width="3" stroke-dasharray="0 8" stroke-linecap="round"/>
    </svg>
    <div class="photo" role="img" aria-label="Photo of three smiling students standing together" style="left:189px;top:30px;width:270px;height:270px;background:radial-gradient(circle at 50% 45%,#6a5a55,#2e2624 70%)"></div>
    <div class="abs logo-disc">Lantern 7</div>
    <h1 class="abs cover-kicker"><span class="big">ARTS</span><span class="small">EDUCATION</span><span class="small">NON-PROFIT</span></h1>
    <h2 class="abs band-title">A Year with Lantern 7</h2>
    <p class="abs intro">Lantern 7 (L7) equips educators and artists to help young people learn and lead with curiosity, deep listening, and imagination. We envision a world where community and civic engagement replace loneliness and isolation. We are creating this world student by student, school by school, story by story. Join us at lantern7.example.</p>
    <h2 class="abs band-outcomes">Outcomes</h2>
    <p class="abs outcomes-lead">A Lantern 7 school partnership ensures that every student and teacher understands:</p>
    <div class="abs outcomes">
      <ul>
        <li>Who I am matters.</li>
        <li>I already know many things.</li>
        <li>I belong to a community who cares about me.</li>
        <li>I can pay attention to my feelings and make choices in how to behave.</li>
        <li>I know when to stop and take care of myself.</li>
        <li>When challenges arise, I know I can handle them, either on my own or with the help of others.</li>
      </ul>
      <ul>
        <li>I can sustain attention to other people's experience.</li>
        <li>I understand my responsibility for the well-being of others.</li>
        <li>I can learn from and teach other people.</li>
        <li>I can find joy and purpose in a variety of ways.</li>
        <li>I understand that discovering my strengths sometimes involves hard work.</li>
        <li>I can improve my life and the lives of others.</li>
      </ul>
    </div>
    <span class="abs footer-text footer-call">CALL US-555 0100 247</span>
    <span class="abs footer-text footer-web">www.lantern7.example</span>
  </section>

  <!-- Page 2: phases -->
  <section class="page page--phases">
    <svg class="page__art" viewBox="0 0 508 715" aria-hidden="true">
      <rect x="0" y="0" width="264" height="140" fill="var(--purple)"/>
      <rect x="264" y="0" width="244" height="140" fill="var(--red)"/>
      <circle cx="510" cy="118" r="62" fill="var(--red-deep)"/>
      <circle cx="510" cy="118" r="74" fill="none" stroke="var(--mustard)" stroke-width="3" stroke-dasharray="0 8" stroke-linecap="round"/>
      <circle cx="40" cy="-5" r="52" fill="none" stroke="var(--mustard)" stroke-width="3" stroke-dasharray="0 8" stroke-linecap="round"/>
      <circle cx="264" cy="28" r="177" fill="var(--purple)"/>
      <path d="M0 676 Q254 632 508 676 L508 715 L0 715Z" fill="var(--red)"/>
      <path d="M0 681 Q254 642 508 681 L508 715 L0 715Z" fill="var(--purple)"/>
      <rect x="279" y="670" width="229" height="45" fill="var(--violet)"/>
      <path d="M0 681 Q254 642 508 681 L508 660 L0 660Z" fill="var(--white)"/>
      <path d="M0 676 Q254 632 508 676 L508 681 Q254 642 0 681Z" fill="var(--red)"/>
      <circle cx="22" cy="700" r="36" fill="var(--red)"/>
      <circle cx="22" cy="700" r="48" fill="none" stroke="var(--mustard)" stroke-width="3" stroke-dasharray="0 8" stroke-linecap="round"/>
    </svg>
    <div class="photo" role="img" aria-label="Portrait photo of a smiling educator" style="left:94px;top:-142px;width:340px;height:340px;background:radial-gradient(circle at 50% 70%,#b08a6c,#3f4a36 75%)"></div>
    <p class="abs lead">L7 supports the growth of the whole individual: as learners and as human beings. We do this work in three phases over the course of a yearlong engagement. L7 customizes your plan to address the specific needs and interests of your school community</p>
    <div class="abs phase-box"></div>
    <h2 class="abs pill pill--red">Phase 1: L7 Community Skills</h2>
    <p class="abs phase-intro">The work of Phase 1 is to create the necessary conditions for student risk-taking and growth. Students develop a positive sense of self and community through hands-on L7 activities, videos, readings, and journaling. Experts in education and psychology offer strategies in deep listening, self-awareness, self-management, social awareness, relationship skills, and responsible decision-making.</p>

    <div class="abs skill skill-1">
      <h3 class="purple">Skill 1: Know yourself</h3>
      <ul>
        <li>Practice self-care</li>
        <li>Know how to self-monitor and self-calm.</li>
        <li>Recognize your own strengths and needs.</li>
      </ul>
    </div>
    <div class="abs divider" style="left:194px;top:366px;height:72px"></div>
    <div class="abs skill skill-2">
      <h3 class="red">Skill 2: Commit to positive relationships</h3>
      <div class="cols">
        <ul>
          <li>Practice deep listening. Self-monitor for a loss of focus. Use techniques to bring your attention back.</li>
          <li>Create space for all emotions in constructive ways. Embrace discomfort.</li>
        </ul>
        <ul>
          <li>Be accountable to learning about different experiences and making connections with people who are different from you.</li>
          <li>Self-monitor for unconscious biases.</li>
        </ul>
      </div>
    </div>

    <div class="abs skill skill-3">
      <h3 class="red">Skill 3: Define how you want your community to treat one another.</h3>
      <ul>
        <li>Recognize neurodiverse ways of engagement</li>
        <li>Practice neutrality to what's being discussed but not to how people treat one another.</li>
      </ul>
    </div>
    <div class="abs divider" style="left:240px;top:462px;height:80px"></div>
    <div class="abs skill skill-4">
      <h3 class="purple">Skill 4: Reflect with the goal of continuous improvement.</h3>
      <p>Day 1 of School: Building Community, Mara Quill, Cultural Wealth Survey, Dev Ashton, Self-Awareness Activities, Otto Brenn, Relationship Skills, Otto Brenn, Story of Self, Story of Community, Ines Varga</p>
    </div>

    <h2 class="abs pill pill--mustard">Phase 2: L7 Story Exchange</h2>
    <p class="abs phase2-text"><strong>IN PHASE 2,</strong> students experience the L7 Story Exchange and learn how they can create and receive the benefits of a positive community. L7 scaffolds the experience based on your community – ensuring a successful exchange for elementary students, multilingual students, etc.</p>
    <span class="abs footer-text footer-call" style="top:682px;width:270px">CALL US-555 0100 247</span>
    <span class="abs footer-text footer-web" style="top:682px;left:290px">www.lantern7.example</span>
  </section>

</main>
</body>
</html>
```